Milo's Sweet Harbor Package Design

A logo has already been made and now i need to incorporate that logo into a package design. Milo's Sweet Harbor products will be sold in retail stores and its package should appeal to both adults and children. Milo's Sweet Harbor sells candy, nuts and other snacks. Files attached will be logo files and pictures of similar package. Please refer to the files for package design. The physical package consists of a printed card (5.75 inches X 4 inches) and a plastic bag. The card is folded over the plastic bag, sealed and hole punched. The design on the card(5.75 inches X 4 inches) should consist of the logo, price(in this case it is $1.99 however it will vary for other products) and product type (in this case its apple(however it will change for other products). On the "back side"(the card is folded down the middle over the plastic and the top of the card becomes the back side, notice how in the example the top half is upside down, this is correct) should include nutrition facts, ingredients, a UPC barcode and the company information(again these vary depending on the product except for the company information that will be same for all products. Company info - "Packaged & Distributed By: Brevik Treats Supply
7142 Larchmont Ave Suite 208 Sterling Heights, Michigan 48592 586-555-0173"

TO WHOEVER WINS THE CONTEST WE WILL COMMISSION YOU TO USE THE SAME DESIGN AND ADD THE NECESSARY INFORMATION(upc, ingredients list, nutritional facts, etc) FOR THE MULTIPLE FLAVORS THAT WE WILL BE PRODUCING UNDER THE Milo's Sweet Harbor BRAND.

```html
<!DOCTYPE html>
<html lang="en">
<head>
<meta charset="utf-8">
<title>Milo Candy Pack</title>
<link rel="stylesheet" href="https://fonts.googleapis.com/css2?family=Open+Sans:wght@400;600;700;800&family=Playfair+Display:wght@700;800&family=Ribeye&family=Libre+Franklin:wght@400;700;900&display=swap">
<style>
  :root {
    --pink: #f5a7a2;
    --pink-light: #fbc9c3;
    --pink-deep: #ee8c86;
    --scallop: #fde3e5;
    --scallop-edge: #e7a1a8;
    --crimson: #a71f3e;
    --ink: #1b1b1b;
    --white: #ffffff;
    --page: #ffffff;
  }
  * { box-sizing: border-box; margin: 0; padding: 0; }
  html, body { width: 884px; height: 1200px; overflow: hidden; background: var(--page); }
  .sheet { position: relative; width: 884px; height: 1200px; }

  .sheet-title {
    position: absolute; top: 10px; left: 0; width: 100%;
    text-align: center; font: 800 25px/1 "Open Sans", sans-serif; color: var(--ink);
  }

  .card-panel {
    position: absolute; overflow: hidden;
    box-shadow: 0 10px 14px -8px rgba(0,0,0,.35);
  }
  .card-panel::before, .card-panel::after {
    content: ""; position: absolute; top: 0; bottom: 0; width: 12px; z-index: 5;
    background: radial-gradient(circle at 0 50%, var(--scallop) 5px, var(--scallop-edge) 6px, transparent 7px) 0 0 / 12px 15px repeat-y;
  }
  .card-panel::before { left: 0; }
  .card-panel::after { right: 0; transform: scaleX(-1); }
  .panel-front { left: 57px; top: 61px; width: 783px; height: 269px; }
  .panel-back  { left: 57px; top: 360px; width: 783px; height: 269px; }
  .panel-folded { left: 118px; top: 678px; width: 679px; height: 472px; }

  .fold-half { position: absolute; left: 0; width: 679px; height: 236px; overflow: hidden; }
  .fold-half.is-top { top: 0; }
  .fold-half.is-bottom { top: 236px; }
  .fold-half .face { transform-origin: 0 0; }
  .fold-half.is-top .face { transform: translate(679px, 236px) rotate(180deg) scale(0.867, 0.877); }
  .fold-half.is-bottom .face { transform: scale(0.867, 0.877); }

  .face {
    position: absolute; left: 0; top: 0; width: 783px; height: 269px; overflow: hidden;
    background:
      radial-gradient(ellipse 60% 90% at 30% 20%, rgba(255,255,255,.28), transparent 70%),
      linear-gradient(100deg, var(--pink-deep) 0%, var(--pink) 35%, var(--pink-light) 60%, var(--pink) 85%, var(--pink-deep) 100%);
  }
  .face-waves { position: absolute; inset: 0; width: 100%; height: 100%; }

  /* front */
  .brand-badge {
    position: absolute; left: 96px; top: 6px; width: 166px; height: 166px; border-radius: 50%;
    background: var(--white); display: flex; align-items: center; justify-content: center;
    text-align: center; padding: 20px;
    font: 800 25px/1.15 "Open Sans", sans-serif; color: var(--crimson);
  }
  .candy-row {
    position: absolute; left: 10px; top: 206px; width: 535px; height: 63px;
    border-radius: 30px 30px 0 0;
    background: linear-gradient(90deg, #d9283c 0%, #f0b12e 12%, #f6c7d6 22%, #e24b4b 34%, #ffffff 42%, #8cc46a 52%, #ffffff 60%, #f28a1f 72%, #f7a928 82%, #e53a3a 92%, transparent 100%);
    opacity: .9;
  }
  .price-tag {
    position: absolute; left: 537px; top: 31px; width: 146px; height: 146px; border-radius: 50%;
    background: var(--white); border: 3px dotted #f4c2c0; outline: 4px solid var(--white);
    display: flex; align-items: center; justify-content: center;
    font: 800 50px/1 "Playfair Display", serif; color: var(--crimson); letter-spacing: -1px;
  }
  .price-tag sup { font-size: 30px; margin-top: -10px; letter-spacing: 0; }
  .corner-sweep { position: absolute; inset: 0; width: 100%; height: 100%; }
  .flavor-front {
    position: absolute; left: 650px; top: 216px;
    font: 400 31px/1 "Ribeye", serif; color: var(--ink);
  }

  /* back */
  .nutrition {
    position: absolute; left: 32px; top: 15px; width: 166px;
    background: var(--white); border: 1px solid var(--ink); padding: 3px 4px 3px;
    font-family: "Libre Franklin", sans-serif; color: var(--ink);
  }
  .nutrition-title { font: 900 17px/1 "Libre Franklin", sans-serif; letter-spacing: .2px; border-bottom: 1px solid var(--ink); padding-bottom: 2px; }
  .nutrition-servings { font-size: 7.5px; margin-top: 2px; }
  .nutrition-size { display: flex; justify-content: space-between; font-size: 8.5px; font-weight: 700; border-bottom: 5px solid var(--ink); padding-bottom: 1px; }
  .nutrition-amount { font-size: 6.5px; font-weight: 700; margin-top: 1px; }
  .nutrition-calories { display: flex; justify-content: space-between; font: 900 15px/1 "Libre Franklin", sans-serif; border-bottom: 3px solid var(--ink); padding-bottom: 1px; }
  .nutrition-dv { text-align: right; font-size: 5.5px; font-weight: 700; border-bottom: 1px solid var(--ink); padding: 1px 0; }
  .nutrition-row { display: flex; justify-content: space-between; font-size: 7px; line-height: 10px; border-bottom: 1px solid var(--ink); }
  .nutrition-row b { font-weight: 700; }
  .nutrition-row.is-sub { padding-left: 8px; }
  .nutrition-row.is-subsub { padding-left: 16px; }
  .nutrition-row.is-last { border-bottom: 4px solid var(--ink); }
  .nutrition-note { font-size: 5px; line-height: 6.5px; padding-top: 2px; }
  .nutrition-note + .nutrition-note { border-top: 1px solid var(--ink); margin-top: 2px; }

  .flavor-back {
    position: absolute; left: 0; width: 783px; top: 16px; text-align: center;
    font: 400 25px/1 "Ribeye", serif; color: var(--ink);
  }
  .brand-mini {
    position: absolute; left: 350px; top: 58px; width: 84px; height: 84px; border-radius: 50%;
    background: var(--white); display: flex; align-items: center; justify-content: center;
    text-align: center; padding: 8px; font: 800 12px/1.15 "Open Sans", sans-serif; color: var(--crimson);
  }
  .distributor {
    position: absolute; left: 0; width: 783px; top: 180px; text-align: center;
    font: 400 12px/16.5px "Open Sans", sans-serif; color: var(--ink);
  }
  .ingredients { position: absolute; right: 16px; top: 18px; width: 260px; text-align: right; color: var(--ink); }
  .ingredients-title { text-align: center; padding-left: 40px; font: 700 15px/1 "Open Sans", sans-serif; margin-bottom: 12px; }
  .ingredients-list { font: 400 12px/17px "Open Sans", sans-serif; }
  .upc-area {
    position: absolute; right: 14px; top: 178px; width: 176px; height: 84px;
    background: var(--white);
  }
</style>
</head>
<body>
<main class="sheet">
  <h1 class="sheet-title">MILO CANDY PACK</h1>

  <section class="card-panel panel-front" aria-label="Front of card">
    <div class="face face-front">
      <svg class="face-waves" viewBox="0 0 783 269" preserveAspectRatio="none" aria-hidden="true">
        <path d="M0 70 C180 20 360 150 560 80 S783 40 783 40 V0 H0Z" fill="#fff" opacity=".12"/>
        <path d="M200 269 C330 170 480 200 620 110 S783 60 783 60 V269Z" fill="#fff" opacity=".1"/>
      </svg>
      <div class="brand-badge">Milo's Sweet Harbor</div>
      <div class="candy-row" role="img" aria-label="Row of assorted wrapped candies, lollipops and peppermints"></div>
      <svg class="corner-sweep" viewBox="0 0 783 269" aria-hidden="true">
        <line x1="610" y1="175" x2="610" y2="262" stroke="#fff" stroke-width="4"/>
        <path d="M560 269 C650 262 730 230 783 150 V269Z" fill="#fff"/>
      </svg>
      <div class="price-tag">$1<sup>.99</sup></div>
      <div class="flavor-front">APPLE</div>
    </div>
  </section>

  <section class="card-panel panel-back" aria-label="Back of card">
    <div class="face face-back">
      <svg class="face-waves" viewBox="0 0 783 269" preserveAspectRatio="none" aria-hidden="true">
        <path d="M0 60 C200 10 380 140 560 70 S783 30 783 30 V0 H0Z" fill="#fff" opacity=".12"/>
        <path d="M150 269 C300 180 470 210 620 130 S783 80 783 80 V269Z" fill="#fff" opacity=".1"/>
      </svg>
      <div class="nutrition">
        <div class="nutrition-title">Nutrition Facts</div>
        <div class="nutrition-servings">6 servings per container</div>
        <div class="nutrition-size"><span>Serving size</span><span>10 pcs (10g)</span></div>
        <div class="nutrition-amount">Amount Per Serving</div>
        <div class="nutrition-calories"><span>Calories</span><span>110</span></div>
        <div class="nutrition-dv">% Daily Value*</div>
        <div class="nutrition-row"><span><b>Total Fat</b> 2.5g</span><b>3%</b></div>
        <div class="nutrition-row is-sub"><span>Saturated Fat 1g</span><b>5%</b></div>
        <div class="nutrition-row is-sub"><span>Trans Fat 0g</span><span></span></div>
        <div class="nutrition-row"><span><b>Sodium</b> 10mg</span><b>0%</b></div>
        <div class="nutrition-row"><span><b>Total Carbohydrate</b> 22g</span><b>8%</b></div>
        <div class="nutrition-row is-sub"><span>Dietary Fiber 0g</span><b>0%</b></div>
        <div class="nutrition-row is-sub"><span>Total Sugars 16g</span><span></span></div>
        <div class="nutrition-row is-subsub"><span>Includes 0g Added Sugars</span><b>0%</b></div>
        <div class="nutrition-row is-last"><span><b>Protein</b> 0g</span><span></span></div>
        <p class="nutrition-note">Not a significant source of cholesterol, vitamin D, calcium, iron, and potassium</p>
        <p class="nutrition-note">*The % Daily Value (DV) tells you how much a nutrient in a serving of food contributes to a daily diet. 2,000 calories a day is used for general nutrition advice.</p>
      </div>
      <div class="flavor-back">APPLE</div>
      <div class="brand-mini">Milo's Sweet Harbor</div>
      <p class="distributor">Packaged &amp; Distributed By:<br>Brevik Treats Supply<br>7142 Larchmont Ave<br>Suite 208 Sterling Heights,<br>Michigan 48592 586-555-0173</p>
      <div class="ingredients">
        <div class="ingredients-title">INGREDIENTS</div>
        <p class="ingredients-list">Sugar, Corn Syrup, Palm Oil,<br>Condensed Skim Milk, Whey,<br>Malic Acid, Artificial Flacors<br>Soy Lecithin, Artificial Colors</p>
      </div>
      <div class="upc-area" role="img" aria-label="UPC barcode area"></div>
    </div>
  </section>

  <section class="card-panel panel-folded" aria-label="Full card, folded layout">
    <div class="fold-half is-top">
      <div class="face face-back">
        <svg class="face-waves" viewBox="0 0 783 269" preserveAspectRatio="none" aria-hidden="true">
          <path d="M0 60 C200 10 380 140 560 70 S783 30 783 30 V0 H0Z" fill="#fff" opacity=".12"/>
          <path d="M150 269 C300 180 470 210 620 130 S783 80 783 80 V269Z" fill="#fff" opacity=".1"/>
        </svg>
        <div class="nutrition">
          <div class="nutrition-title">Nutrition Facts</div>
          <div class="nutrition-servings">6 servings per container</div>
          <div class="nutrition-size"><span>Serving size</span><span>10 pcs (10g)</span></div>
          <div class="nutrition-amount">Amount Per Serving</div>
          <div class="nutrition-calories"><span>Calories</span><span>110</span></div>
          <div class="nutrition-dv">% Daily Value*</div>
          <div class="nutrition-row"><span><b>Total Fat</b> 2.5g</span><b>3%</b></div>
          <div class="nutrition-row is-sub"><span>Saturated Fat 1g</span><b>5%</b></div>
          <div class="nutrition-row is-sub"><span>Trans Fat 0g</span><span></span></div>
          <div class="nutrition-row"><span><b>Sodium</b> 10mg</span><b>0%</b></div>
          <div class="nutrition-row"><span><b>Total Carbohydrate</b> 22g</span><b>8%</b></div>
          <div class="nutrition-row is-sub"><span>Dietary Fiber 0g</span><b>0%</b></div>
          <div class="nutrition-row is-sub"><span>Total Sugars 16g</span><span></span></div>
          <div class="nutrition-row is-subsub"><span>Includes 0g Added Sugars</span><b>0%</b></div>
          <div class="nutrition-row is-last"><span><b>Protein</b> 0g</span><span></span></div>
          <p class="nutrition-note">Not a significant source of cholesterol, vitamin D, calcium, iron, and potassium</p>
          <p class="nutrition-note">*The % Daily Value (DV) tells you how much a nutrient in a serving of food contributes to a daily diet. 2,000 calories a day is used for general nutrition advice.</p>
        </div>
        <div class="flavor-back">APPLE</div>
        <div class="brand-mini">Milo's Sweet Harbor</div>
        <p class="distributor">Packaged &amp; Distributed By:<br>Brevik Treats Supply<br>7142 Larchmont Ave<br>Suite 208 Sterling Heights,<br>Michigan 48592 586-555-0173</p>
        <div class="ingredients">
          <div class="ingredients-title">INGREDIENTS</div>
          <p class="ingredients-list">Sugar, Corn Syrup, Palm Oil,<br>Condensed Skim Milk, Whey,<br>Malic Acid, Artificial Flacors<br>Soy Lecithin, Artificial Colors</p>
        </div>
        <div class="upc-area" role="img" aria-label="UPC barcode area"></div>
      </div>
    </div>
    <div class="fold-half is-bottom">
      <div class="face face-front">
        <svg class="face-waves" viewBox="0 0 783 269" preserveAspectRatio="none" aria-hidden="true">
          <path d="M0 70 C180 20 360 150 560 80 S783 40 783 40 V0 H0Z" fill="#fff" opacity=".12"/>
          <path d="M200 269 C330 170 480 200 620 110 S783 60 783 60 V269Z" fill="#fff" opacity=".1"/>
        </svg>
        <div class="brand-badge">Milo's Sweet Harbor</div>
        <div class="candy-row" role="img" aria-label="Row of assorted wrapped candies, lollipops and peppermints"></div>
        <svg class="corner-sweep" viewBox="0 0 783 269" aria-hidden="true">
          <line x1="610" y1="175" x2="610" y2="262" stroke="#fff" stroke-width="4"/>
          <path d="M560 269 C650 262 730 230 783 150 V269Z" fill="#fff"/>
        </svg>
        <div class="price-tag">$1<sup>.99</sup></div>
        <div class="flavor-front">APPLE</div>
      </div>
    </div>
  </section>
</main>
</body>
</html>
```